Morvela Aesthetic Doctor

I require an elegant, luxurious looking business card for my aesthetic business. I am a doctor and that will set me aside from competitors. I am planning to provide home and spa based treatments to clients with high expectations. I have attached my logo.

```html
<!DOCTYPE html>
<html lang="en">
<head>
<meta charset="utf-8">
<title>Morvela Aesthetic Doctor — Business Card</title>
<link rel="stylesheet" href="https://fonts.googleapis.com/css2?family=Crimson+Pro:wght@400;600;700&display=swap">
<style>
  :root {
    --page-bg: #f5f5f5;
    --card-grey: #444444;
    --card-dark: #1f1f1f;
    --rule-white: #f2f2f2;
    --text-light: #e6e6e6;
    --text-soft: #d0d0d0;
    --accent-blue: #3d9fe0;
    --brand-grey: #c9c9c9;
  }
  * { box-sizing: border-box; margin: 0; padding: 0; }
  html, body {
    width: 1200px; height: 2291px; overflow: hidden;
    background: var(--page-bg);
    font-family: "Crimson Pro", Georgia, serif;
  }
  .sheet {
    position: relative; width: 1200px; height: 2291px;
  }
  .card {
    position: absolute; left: 135px; width: 930px; height: 531px;
    background: var(--card-grey);
    box-shadow: 0 3px 8px rgba(0,0,0,0.35);
    overflow: hidden;
  }
  .card--front { top: 581px; }
  .card--back { top: 1179px; }

  /* Front */
  .front-brand {
    position: absolute; left: 0; right: 0; top: 150px;
    display: flex; align-items: center; justify-content: center; gap: 22px;
  }
  .brand-dot {
    width: 96px; height: 96px; border-radius: 50%;
    border: 3px solid var(--accent-blue);
  }
  .brand-name {
    color: var(--brand-grey); font-weight: 400; line-height: 1.0;
    letter-spacing: 2px; text-transform: uppercase;
  }
  .front-brand .brand-name { font-size: 50px; }
  .brand-name small { display: block; font-size: 0.6em; letter-spacing: 3px; }
  .tagline {
    position: absolute; left: 0; right: 0; top: 298px;
    text-align: center; color: var(--text-light);
    font-size: 23px; letter-spacing: 0.5px;
  }
  .front-band {
    position: absolute; left: 0; right: 0; top: 408px; bottom: 0;
    border-top: 3px solid var(--rule-white);
    background: var(--card-dark);
  }

  /* Back */
  .back-panel { position: absolute; inset: 0; }
  .back-brand {
    position: absolute; left: 34px; top: 210px;
    display: flex; align-items: center; gap: 14px;
  }
  .back-brand .brand-dot { width: 78px; height: 78px; }
  .back-brand .brand-name { font-size: 36px; }
  .details {
    position: absolute; left: 482px; top: 72px; right: 30px;
    color: var(--text-light);
  }
  .person-name { font-size: 38px; font-weight: 700; line-height: 1; }
  .person-name .credentials {
    font-size: 16px; font-weight: 400; margin-left: 14px; letter-spacing: 0.3px;
  }
  .qualification { font-size: 23px; margin-top: 10px; }
  .contact-list { list-style: none; margin-top: 28px; }
  .contact-list li {
    display: flex; align-items: center; font-size: 22px; height: 39px; letter-spacing: 0.5px;
  }
  .contact-list svg { width: 18px; height: 18px; margin-right: 17px; flex: none; }
  .social { display: inline-flex; gap: 6px; margin-left: 36px; }
  .social span {
    width: 18px; height: 18px; border-radius: 50%; background: var(--accent-blue);
  }
  .services {
    margin-top: 72px; font-size: 19px; line-height: 26px; color: var(--text-soft);
  }
</style>
</head>
<body>
<main class="sheet">

  <section class="card card--front" aria-label="Card front">
    <div class="front-brand">
      <span class="brand-dot"></span>
      <span class="brand-name">Morvela<small>Aesthetic Doctor</small></span>
    </div>
    <p class="tagline">HOME AND SPA BASED TREATMENTS</p>
    <div class="front-band" role="img" aria-label="Dark band with a subtle geometric triangle pattern"></div>
  </section>

  <section class="card card--back" aria-label="Card back">
    <svg class="back-panel" width="930" height="531" viewBox="0 0 930 531">
      <polygon points="0,0 388,0 459,531 0,531" fill="#1f1f1f" role="img" aria-label="Dark panel with a subtle geometric triangle pattern"/>
      <line x1="389" y1="0" x2="460" y2="531" stroke="#f2f2f2" stroke-width="4"/>
    </svg>
    <div class="back-brand">
      <span class="brand-dot"></span>
      <span class="brand-name">Morvela<small>Aesthetic Doctor</small></span>
    </div>
    <div class="details">
      <h1 class="person-name">Dr Lena Varsk<span class="credentials">MRCPCH MD</span></h1>
      <p class="qualification">Australasian Diploma of Aesthetic Medicine</p>
      <ul class="contact-list">
        <li>
          <svg viewBox="0 0 24 24"><path fill="#3d9fe0" d="M6.6 10.8c1.4 2.8 3.8 5.1 6.6 6.6l2.2-2.2c.3-.3.7-.4 1-.2 1.1.4 2.3.6 3.6.6.6 0 1 .4 1 1V20c0 .6-.4 1-1 1C10.6 21 3 13.4 3 4c0-.6.4-1 1-1h3.5c.6 0 1 .4 1 1 0 1.3.2 2.5.6 3.6.1.3 0 .7-.2 1z"/></svg>
          0800 555 014
        </li>
        <li>
          <svg viewBox="0 0 24 24"><rect x="2" y="5" width="20" height="14" fill="#3d9fe0"/><path d="M2 5l10 8 10-8" fill="none" stroke="#444" stroke-width="2"/></svg>
          lena@morvela.co.nz
        </li>
        <li>
          <svg viewBox="0 0 24 24" fill="none" stroke="#3d9fe0" stroke-width="2"><circle cx="12" cy="12" r="9"/><path d="M3 12h18M12 3c3 3 3 15 0 18M12 3c-3 3-3 15 0 18"/></svg>
          www.morvela.co.nz
          <span class="social" aria-label="Social media"><span></span><span></span></span>
        </li>
      </ul>
      <p class="services">Dermal injectables - Plasma facials - Microneedling<br>Skin boosters - Excessive sweating Home and Spa<br>Based Treatments</p>
    </div>
  </section>

</main>
</body>
</html>
```